A Business Card and Letterhead for a Surgeon in Practice

Design a Business Card and Business Letterhead with theming consistent with my website, logo and referral pad which will be uploaded for reference.

Website found at: www.bertramholvey.com.au

A text file is uploaded indicating what information needs to be on the business card and a separate document for the letterhead.

The other images I have uploaded are entirely optional for artistic design. None of them necessarily have to be used. Further imagery may or may not be included as per the designer to get the best result
Updates

Industry/Entity Type

Medical

Requirements
Must have
• Logo as uploaded. Certain text as uploaded.
• NEW as of 8th August:
• **On the back there needs to be a blank space incorporating at least half of the vertical distance of the card - this is where stickers can be placed in the office for certain appointment details**
• **Also, for the consulting locations a small box next to each should be included so that it can be ticked by my secretary indicating the correct location**

```html
<!DOCTYPE html>
<html lang="en">
<head>
<meta charset="utf-8">
<title>Bertram Holvey – Letterhead</title>
<link rel="stylesheet" href="https://fonts.googleapis.com/css2?family=Source+Sans+3:wght@400;600&display=swap">
<style>
  :root {
    --paper: #f7f6f4;
    --teal: #1e8a83;
    --teal-soft: rgba(120, 190, 185, 0.22);
    --ink: #4d4d4d;
    --ink-light: #6a6a6a;
    --rule: #8a8a8a;
  }
  * { margin: 0; padding: 0; box-sizing: border-box; }
  html, body { width: 872px; height: 1200px; overflow: hidden; }
  body {
    background: var(--paper);
    font-family: "Source Sans 3", Arial, sans-serif;
    color: var(--ink);
    position: relative;
  }
  .backdrop-swirl {
    position: absolute; left: 240px; top: 560px; width: 632px; height: 640px;
    background: radial-gradient(ellipse at 70% 60%, var(--teal-soft), rgba(200,200,200,0.12) 55%, transparent 75%);
  }
  .brand { position: absolute; left: 78px; top: 80px; display: flex; align-items: center; gap: 20px; }
  .brand-dot { width: 62px; height: 62px; border-radius: 50%; background: var(--teal); }
  .brand-name {
    font-size: 36px; font-weight: 600; color: var(--teal);
    letter-spacing: 1px; line-height: 1;
  }
  .brand-tagline {
    font-size: 11.5px; letter-spacing: 2.4px; text-transform: uppercase;
    color: var(--ink-light); margin-top: 5px;
  }
  .column-rule {
    position: absolute; left: 320px; top: 175px; width: 1px; height: 925px;
    background: var(--rule);
  }
  .sidebar {
    position: absolute; left: 97px; top: 527px; width: 210px;
    font-size: 11.8px; line-height: 16.4px; color: var(--ink);
  }
  .sidebar p { margin-bottom: 11px; }
  .sidebar .label { color: var(--teal); font-weight: 600; }
  .sidebar h3 {
    font-size: 12px; font-weight: 600; color: var(--teal);
    text-transform: uppercase; letter-spacing: 0.3px; margin: 4px 0 5px;
  }
  .sidebar ul { list-style: none; margin-bottom: 8px; }
  .sidebar li { padding-left: 12px; position: relative; }
  .sidebar li::before {
    content: ""; position: absolute; left: 2px; top: 6px; width: 5px; height: 5px;
    border-radius: 50%; background: var(--teal);
  }
  .sidebar li.region { padding-left: 14px; color: var(--teal); font-weight: 600; }
  .sidebar li.region::before {
    border-radius: 0; width: 0; height: 0; background: none; top: 4px; left: 0;
    border-left: 5px solid transparent; border-right: 5px solid transparent;
    border-bottom: 9px solid var(--teal);
  }
  .sidebar .doctor { color: var(--teal); font-weight: 600; text-transform: uppercase; margin-top: 6px; }
  .letter {
    position: absolute; left: 359px; top: 205px; width: 422px;
    font-size: 13.6px; line-height: 20.5px; color: var(--ink);
  }
  .letter .salutation { font-size: 23px; line-height: 28px; margin-bottom: 48px; color: #555; }
  .letter p.body { text-align: justify; hyphens: auto; margin-bottom: 20.5px; }
  .letter .closing { margin-top: 40px; }
  .signature {
    position: absolute; left: 357px; top: 1058px; width: 112px; height: 44px;
    background: linear-gradient(90deg, rgba(40,40,40,0.25), rgba(40,40,40,0.08));
    border-radius: 4px;
  }
</style>
</head>
<body>
  <div class="backdrop-swirl" role="img" aria-label="Faint decorative brand swirl in soft teal and grey"></div>

  <header class="brand">
    <div class="brand-dot"></div>
    <div>
      <div class="brand-name">BERTRAM HOLVEY</div>
      <div class="brand-tagline">General, Upper GI &amp; Bariatric Surgeon</div>
    </div>
  </header>

  <div class="column-rule"></div>

  <aside class="sidebar">
    <p>Fairhaven Eastern Hospital<br>Suite 14, 3rd Floor<br>22 Harrow St, Box Hill 3128</p>
    <p><span class="label">Tel:</span> 03 9555 0142<br><span class="label">Fax:</span> 03 9555 0143</p>
    <p><span class="label">Paging Service :</span> 0400 555 217<br><span class="label">Provider No.</span> 418273KM</p>
    <h3>Consulting Locations</h3>
    <ul>
      <li class="region">Melbourne</li>
      <li>Collins St CBD</li>
      <li>Box Hill</li>
      <li>Rowville</li>
      <li class="region">Regional</li>
      <li>Bendigo</li>
      <li>Kyneton</li>
      <li>Latrobe Valley</li>
    </ul>
    <h3>Operating</h3>
    <ul>
      <li>Fairhaven Eastern</li>
      <li>Fairhaven Richmond</li>
      <li>Box Hill</li>
      <li>South Gippsland</li>
    </ul>
    <h3>Services</h3>
    <ul>
      <li>Bariatric Surgery</li>
      <li>General Surgery</li>
      <li>Antireflux Surgery</li>
      <li>Body Contouring Surgery</li>
    </ul>
    <p>All Appointments &amp; Correspondence<br>to Box Hill Rooms</p>
    <div class="doctor">Dr Bertram Holvey</div>
    <div>ABN 48 512 604 117</div>
    <div>info@bayviewweightsurgery.com.au</div>
  </aside>

  <main class="letter">
    <div class="salutation">Dear Mr. Smith,</div>
    <p class="body">Lorem ipsum dolor sit amet, consectetur adipiscing elit. Donec orci purus, luctus vitae dignissim eu, iaculis sed purus. Vivamus faucibus, ipsum nec aliquet viverra, leo mauris condimentum ligula, sit amet sagittis enim ligula quis arcu. Nam egestas tortor id nisi porttitor mattis. In tortor ante, ultricies in suscipit a, tempus non massa. Vivamus et auctor mi. Fusce vel massa nulla. Phasellus nec eros mauris, et scelerisque orci.</p>
    <p class="body">Donec malesuada orci vitae nulla accumsan porta a id massa. Quisque accumsan iaculis magna sit amet fringilla. Maecenas consequat, magna eget tincidunt semper, odio nibh rutrum mi, id feugiat ante nisi eu risus. Vestibulum nunc orci, rhoncus a placerat in, ultricies in mi. Cras mattis varius eros, vel fringilla nisi suscipit eget. Quisque scelerisque sagittis nulla at porttitor.</p>
    <p class="body">Sed id augue vitae urna euismod commodo aliquet a quam. Pellentesque arcu velit, cursus et malesuada ut, consequat et diam. Nullam erat sem, rhoncus id ullamcorper vitae, rhoncus et arcu. In ultricies ultricies nulla, ut rutrum nisi iaculis at. Donec eu magna a metus ornare faucibus. Fusce aliquet faucibus ultricies. Morbi semper, est id tincidunt gravida, sem arcu adipiscing lacus, ac bibendum nulla leo eu purus. Quisque nec diam sed risus consectetur a ccumsan quis quis nibh. Vestibulum id purus lorem.</p>
    <p class="body">Sed id augue vitae urna euismod commodo aliquet a quam. Pellentesque arcu velit, cursus et malesuada ut, consequat et diam. Nullam erat sem, rhoncus id ullamcorper vitae, rhoncus et arcu. In ultricies ultricies nulla, ut rutrum nisi iaculis at. Donec eu magna a metus ornare faucibus. Fusce aliquet faucibus ultricies. Morbi semper, est id tincidunt</p>
    <p class="body">It is a long established fact that a reader will be distracted by the readable content of a page when looking at its layout. The point of using Lorem Ipsum is that it has a more-or-less normal distribution of letters, as opposed to using 'Content here, content here', making it look like readable English. Many desktop publishing packages</p>
    <p class="closing">Sincerely,</p>
  </main>

  <div class="signature" role="img" aria-label="Handwritten signature"></div>
</body>
</html>
```